Talwick Orsine Beauty brand redesign of product labels

national rebrand of skincare product labels - same design but 6 sizes. Will be used for facial serums, body oils, bath salts, room sprays, etc. All labels to be same design - just adjusted for the different sizes. See brand document and sample label.

Bottle Specifications are located in the branding file.
Fonts included in product branding document.
Colours included in branding document.

Featuring company name and logo, product name, product feature, ingredients, size, directions, tag line. See attached sample label as example for design.

Black label base - matt.

Target Market(s)

Natural beauty, 20-60

Industry/Entity Type

farming, natural beauty

Font styles to use
Sans Serif

Requirements
Must have
• Modern, clean, homey
Nice to have
• modern clean design - using the branding colours provided
Should not have
• busy, crowded,

```html
<!DOCTYPE html>
<html lang="en">
<head>
<meta charset="utf-8">
<title>Talwick Orsine Beauty – Solenne Label</title>
<link rel="stylesheet" href="https://fonts.googleapis.com/css2?family=Arimo:wght@400&family=Dancing+Script:wght@500&display=swap">
<style>
  :root {
    --backdrop: #e9ecee;
    --label-black: #0c0c0c;
    --brand-teal: #74a9a2;
    --sage: #bcd3a8;
    --rule-white: #f4f4f4;
    --text-white: #eeeeee;
  }
  * { margin: 0; padding: 0; box-sizing: border-box; }
  html, body { width: 1200px; height: 1200px; overflow: hidden; }
  body {
    background: var(--backdrop);
    font-family: "Arimo", Arial, sans-serif;
    position: relative;
  }
  .label {
    position: absolute;
    left: 280px; top: 95px;
    width: 640px; height: 1010px;
    background: var(--label-black);
    text-align: center;
  }
  .brand {
    position: absolute;
    left: 0; right: 0; top: 150px;
    display: flex;
    justify-content: center;
    align-items: center;
    gap: 16px;
  }
  .brand-mark {
    flex: none;
    width: 22px; height: 22px;
    border: 2px solid var(--brand-teal);
    border-radius: 50%;
  }
  .brand-name {
    color: var(--brand-teal);
    font-size: 26px;
    letter-spacing: 4px;
    line-height: 1.3;
    text-transform: uppercase;
    white-space: nowrap;
  }
  .product-name {
    position: absolute;
    left: 0; right: 0; top: 318px;
    font-family: "Dancing Script", cursive;
    font-weight: 500;
    font-size: 128px;
    line-height: 1;
    color: var(--brand-teal);
  }
  .product-feature {
    position: absolute;
    left: 0; right: 0; top: 498px;
    color: var(--sage);
    font-size: 34px;
    line-height: 1.25;
    text-transform: uppercase;
  }
  .divider {
    position: absolute;
    left: 87px; right: 87px; top: 716px;
    height: 3px;
    background: var(--rule-white);
  }
  .product-type {
    position: absolute;
    left: 0; right: 0; top: 772px;
    color: var(--text-white);
    font-size: 26px;
    text-transform: uppercase;
  }
  .product-size {
    position: absolute;
    left: 0; right: 0; top: 840px;
    color: var(--sage);
    font-size: 38px;
  }
</style>
</head>
<body>
  <main class="label">
    <div class="brand">
      <span class="brand-mark"></span>
      <span class="brand-name">Talwick Orsine<br>Beauty</span>
    </div>
    <h1 class="product-name">Solenne</h1>
    <p class="product-feature">Natural Coconut Oil<br>Face Wash</p>
    <div class="divider"></div>
    <p class="product-type">Consentrated Soothing Mist</p>
    <p class="product-size">1.0fl oz/ 30ml</p>
  </main>
</body>
</html>
```